UI/UX Re-Do for Velmora - a free to use project management platform for desktop and mobile.

UI/UX Re-Do for Velmora
Velmora is a free to use project management platform for desktop and mobile.
We are looking for help with our UI/UX re-design.
As of now the platform is totally functional.
The problem is around flow and look. We want VM to become something that any one can use to manage and even socialize any project. A project can be something work related like organizing a team around a software build, marketing campaign, shared client file space, etc... In fact, most of our current members are using VM for just such work projects.
We also see a project as planning a wedding, organizing a group trip, a simple to-do list, organizing a kids sports team, and so on...
To become a platform that people will use in their work and personal life we first need to become more intuitive and friendly - while maintaining advanced functionality for more advanced needs.
We need help to beautify, streamline, and simplify - while keeping all the functions.
The quickest way to understand VM, and our current issues is this short video:
https://vidshare-example.net/Kq8TzRw2mLp
For sure see this link for the entire most recent description AND images:
https://velmoraapp-example.com/?p=HtrwN4YcZsD
The best way to understand VM is to actually use it:
https://velmoraapp-example.com
Should you choose to take a run at improving VM here are the details:
Please focus your ideas for mobile, it's where we have the biggest issues.
Feel free to get outside the box.
Avoid swipe oriented designs.
Feel free to focus on ideas over polished outputs.
Use any tool you like, PS, hand drawing, written description if you think that works best.
(FYI - we use mostly use Google Presentation docs internally)
Point is illustration of ideas over tool choice.
Feel free to:
Create something totally new
And/or riff on what we have now
And/or riff on the new design we are considering (see images below)
|||
If we go the direction of the images/designs below the idea is to give people options on how they see/experience VM.
Just below is what we are calling Base Mode. This is a more basic and simple flow. Probably a default to keep new users feeling comfortable at the start.
<img src="https://img.picvault-example.net/8tqWLbN.jpg" style="width: 100%;">
https://img.picvault-example.net/8tqWLbN.jpg
|||
We are calling this optional view Atlas Mode. It is more advanced and can show all project, goal(renamed 'milestones') at the same time. This is more of a paint job on the current design.
<img src="https://img.picvault-example.net/mvdHRsJ.jpg" style="width: 100%;">
https://img.picvault-example.net/mvdHRsJ.jpg
|||
If you're submitting please let us know if you can also do the PS files for dev.
Not required, but once we nail down the concepts we want someone to hone in the PS files.
As an optional bonus we will also be giving credit to you/your company in VM.
Let us know if you do or don't want that.
We are excited to see your work!!
<img src=" " style="width: 100%;">
Target Market(s)
Anyone who needs to organize any project, big or small. The key is to make a super friendly user experience for new users while retaining advanced functions.

```html
<!DOCTYPE html>
<html lang="en">
<head>
<meta charset="utf-8">
<title>Velmora – Base Mode</title>
<link href="https://fonts.googleapis.com/css2?family=Open+Sans:wght@400;600&display=swap" rel="stylesheet">
<style>
:root{
  --search-bg:#0c4aa8;
  --sidebar:#1d3a63;
  --teal:#2a93b8;
  --teal-line:#3aa6c8;
  --orange:#f0801f;
  --card:#ffffff;
  --text:#222;
  --muted:#aab2ba;
  --link:#2a9fd6;
  --footer:#262626;
  --btn-dark:#36434f;
  --ink:#16222e;
  --avatar:#c9ced4;
}
*{box-sizing:border-box;margin:0;padding:0}
html,body{width:1200px;height:816px;overflow:hidden}
body{font-family:"Open Sans",Arial,sans-serif;color:var(--text);position:relative;background:var(--sidebar)}
.app-header{position:absolute;left:0;top:0;width:1200px;height:60px;background:linear-gradient(90deg,#0a7fd4,#0ba0ec 60%,#0a7fe0)}
.brand{position:absolute;left:10px;top:20px;font-size:14px;font-weight:600;color:#fff;line-height:20px}
.menu-toggle{position:absolute;left:72px;top:9px;width:42px;height:42px;border-radius:50%;border:1.5px solid var(--ink);display:flex;align-items:center;justify-content:center}
.search{position:absolute;left:249px;top:11px;width:701px;height:37px;background:var(--search-bg);border:1px solid #2a7fd8;display:flex;align-items:center;padding:0 16px;color:#9fc1ea;font-size:11px}
.search svg{position:absolute;right:14px;top:12px}
.hdr-chip{position:absolute;top:21px;height:18px;border-radius:2px}
.chip-light{background:#9fc0f2}
.chip-dark{background:#174a8a;width:18px}
.sidebar{position:absolute;left:0;top:60px;width:312px;height:695px;background:var(--sidebar)}
.section-head{position:absolute;left:12px;width:288px;height:42px;background:var(--teal);color:#fff;font-size:15.5px;display:flex;align-items:center;padding-left:30px}
.section-head .ico{position:absolute;left:9px;top:14px}
.section-head .caret{position:absolute;right:11px;top:18px}
.project{position:absolute;left:12px;width:288px;height:41px;background:var(--card);border-bottom:2px solid var(--teal-line)}
.project .title{position:absolute;left:30px;top:5px;font-size:13px;color:#2c8fb8}
.project .status{position:absolute;left:31px;top:24px;font-size:7px;color:var(--muted)}
.project .ico{position:absolute;left:11px;top:10px}
.project.active{height:59px;border-bottom:2px solid var(--orange)}
.project.active .title{color:var(--orange)}
.project-actions{position:absolute;left:0;top:35px;width:288px;height:22px;border-top:1px solid #e3e3e3;display:flex}
.project-actions span{flex:1;font-size:7.5px;color:#888;display:flex;align-items:center;justify-content:center;gap:3px;border-right:1px solid #e3e3e3}
.project-actions span:last-child{border-right:none}
.stage{position:absolute;left:312px;top:60px;width:888px;height:695px;background:
 radial-gradient(ellipse 260px 150px at 620px 540px,#d8a58f 0%,rgba(216,165,143,0) 100%),
 radial-gradient(ellipse 300px 200px at 160px 500px,#b79aa0 0%,rgba(183,154,160,0) 100%),
 radial-gradient(ellipse 250px 160px at 330px 80px,#c6a9a3 0%,rgba(198,169,163,0) 100%),
 linear-gradient(160deg,#4f6f8a 0%,#6b7f98 35%,#8e8aa2 60%,#4e6684 100%)}
.notes-select{position:absolute;left:1091px;top:86px;width:96px;height:25px;background:#fff;border:1px solid #ddd;font-size:10.5px;padding:5px 10px}
.notes-select svg{position:absolute;right:8px;top:10px}
.post{position:absolute;left:324px;top:130px;width:863px;height:221px;background:#fff}
.post-head{height:48px;background:#f6f6f6;position:relative}
.avatar{position:absolute;left:12px;top:8px;width:30px;height:30px;border-radius:50%;background:var(--avatar)}
.author{position:absolute;left:50px;top:10px;font-size:11.5px;color:#333}
.stamp{position:absolute;left:49px;top:26px;font-size:8px;color:#555}
.post-links{position:absolute;right:40px;top:18px;font-size:7.5px;color:#666}
.kebab{position:absolute;right:20px;top:14px}
.post-body{padding:21px 12px 0;font-size:9.3px;line-height:11px;color:#222}
.post-body p{margin-bottom:10px}
.doc-link{display:flex;align-items:center;gap:7px;color:var(--link);font-size:11px;margin-top:18px}
.scrollbar{position:absolute;right:2px;top:52px;width:3px;height:164px;background:#ddd}
.composer{position:absolute;left:324px;top:363px;width:863px;height:42px;background:#fff;font-size:9.5px;color:#333;padding:15px 18px}
.round-btn{position:absolute;top:5px;width:31px;height:31px;border-radius:50%;background:var(--btn-dark);display:flex;align-items:center;justify-content:center}
.app-footer{position:absolute;left:0;top:755px;width:1200px;height:61px;background:var(--footer);color:#eee;font-size:9.5px;text-align:center;padding-top:25px}
.build-tag{position:absolute;right:9px;bottom:6px;font-size:9px}
</style>
</head>
<body>
<header class="app-header">
  <div class="brand">Velmora</div>
  <div class="menu-toggle"><svg width="20" height="16" viewBox="0 0 20 16"><rect y="1" width="20" height="2.6" rx="1.3" fill="#16222e"/><rect y="6.7" width="20" height="2.6" rx="1.3" fill="#16222e"/><rect y="12.4" width="20" height="2.6" rx="1.3" fill="#16222e"/></svg></div>
  <div class="search">Search<svg width="12" height="12" viewBox="0 0 12 12"><circle cx="5" cy="5" r="3.8" fill="none" stroke="#dbe8fa" stroke-width="1.6"/><line x1="7.8" y1="7.8" x2="11" y2="11" stroke="#dbe8fa" stroke-width="1.8"/></svg></div>
  <div class="hdr-chip chip-light" style="left:1026px;width:18px"></div>
  <div class="hdr-chip chip-light" style="left:1049px;width:42px"></div>
  <div class="hdr-chip chip-dark" style="left:1122px"></div>
  <div class="hdr-chip chip-dark" style="left:1146px"></div>
  <div class="hdr-chip chip-dark" style="left:1170px"></div>
</header>

<nav class="sidebar">
  <div class="section-head" style="top:15px">
    <svg class="ico" width="14" height="14" viewBox="0 0 14 14"><circle cx="3" cy="7" r="2.4" fill="#fff"/><circle cx="11" cy="3" r="2.4" fill="#fff"/><circle cx="11" cy="11" r="2.4" fill="#fff"/><path d="M3 7 11 3M3 7 11 11" stroke="#fff" stroke-width="1.5"/></svg>
    Current Shared Project
    <svg class="caret" width="10" height="6" viewBox="0 0 10 6"><path d="M0 6 5 0 10 6Z" fill="#fff"/></svg>
  </div>

  <div class="project active" style="top:70px">
    <svg class="ico" width="12" height="12" viewBox="0 0 12 12"><path d="M3.5 3a4.3 4.3 0 1 0 5 0" fill="none" stroke="#f0801f" stroke-width="1.6"/><line x1="6" y1="0.5" x2="6" y2="6" stroke="#f0801f" stroke-width="1.6"/></svg>
    <div class="title">Startup Starter Kit</div>
    <div class="status">Status</div>
    <svg style="position:absolute;right:12px;top:10px" width="12" height="8" viewBox="0 0 12 8"><ellipse cx="6" cy="4" rx="6" ry="3.8" fill="#999"/><circle cx="6" cy="4" r="1.8" fill="#fff"/></svg>
    <div class="project-actions"><span>▲ Hide Goals</span><span>● Join</span><span>⧉ Copy</span></div>
  </div>

  <div class="project" style="top:142px"><svg class="ico" width="11" height="13" viewBox="0 0 11 13"><path d="M1 1h6l3 3v8H1Z" fill="none" stroke="#2c8fb8" stroke-width="1.2"/><path d="M3 6h5M3 8h5M3 10h5" stroke="#2c8fb8"/></svg><div class="title">Meeting Notes / Business SCRUM</div><div class="status">Status</div></div>
  <div class="project" style="top:196px"><svg class="ico" width="13" height="12" viewBox="0 0 13 12"><rect x="5" y="0" width="3" height="3" fill="#2c8fb8"/><rect x="0" y="8" width="3" height="3" fill="#2c8fb8"/><rect x="5" y="8" width="3" height="3" fill="#2c8fb8"/><rect x="10" y="8" width="3" height="3" fill="#2c8fb8"/><path d="M6.5 3v5M1.5 8V5.5h10V8" fill="none" stroke="#2c8fb8"/></svg><div class="title">Corporate Structure</div><div class="status">Status</div></div>
  <div class="project" style="top:250px"><svg class="ico" width="10" height="13" viewBox="0 0 10 13"><text x="1" y="11" font-size="12" font-weight="600" fill="#2c8fb8" font-family="Open Sans, sans-serif">$</text></svg><div class="title">Fund Raising / Corp Dev</div><div class="status">Status</div></div>
  <div class="project" style="top:304px"><svg class="ico" width="14" height="11" viewBox="0 0 14 11"><rect x="0.6" y="1" width="12.8" height="9" fill="none" stroke="#2c8fb8" stroke-width="1.2"/><circle cx="7" cy="5.5" r="2.2" fill="#2c8fb8"/></svg><div class="title">Operating Finance</div><div class="status">Status</div></div>
  <div class="project" style="top:358px"><svg class="ico" width="14" height="12" viewBox="0 0 14 12"><rect x="0" y="3" width="14" height="9" rx="1" fill="#2c8fb8"/><rect x="4.5" y="0.5" width="5" height="3" fill="none" stroke="#2c8fb8"/><rect x="0" y="6.5" width="14" height="1" fill="#fff"/></svg><div class="title">Sales / Business Development</div><div class="status">Status</div></div>
  <div class="project" style="top:412px"><svg class="ico" width="14" height="12" viewBox="0 0 14 12"><path d="M1 4h3l7-4v12L4 8H1Z" fill="#2c8fb8"/></svg><div class="title">Marketing</div><div class="status">Status</div></div>
  <div class="project" style="top:466px"><svg class="ico" width="12" height="12" viewBox="0 0 12 12"><circle cx="6" cy="6" r="5" fill="none" stroke="#2c8fb8" stroke-width="1.5"/><circle cx="6" cy="6" r="2" fill="#2c8fb8"/></svg><div class="title">Other</div><div class="status">Status</div></div>

  <div class="section-head" style="top:519px">
    <svg class="ico" width="16" height="13" viewBox="0 0 16 13"><path d="M0.5 0v12.5H16" fill="none" stroke="#fff"/><rect x="3" y="6" width="2" height="6" fill="#fff"/><rect x="6.5" y="3" width="2" height="9" fill="#fff"/><rect x="10" y="5" width="2" height="7" fill="#fff"/><rect x="13.5" y="2" width="2" height="10" fill="#fff"/></svg>
    Velmora Top Project Picks
    <svg class="caret" width="10" height="6" viewBox="0 0 10 6"><path d="M0 0 5 6 10 0Z" fill="#fff"/></svg>
  </div>
  <div class="section-head" style="top:567px">
    <svg class="ico" width="15" height="14" viewBox="0 0 15 14"><path d="M7.5 0 9.4 4.8 14.5 5.1 10.6 8.4 11.9 13.5 7.5 10.7 3.1 13.5 4.4 8.4 0.5 5.1 5.6 4.8Z" fill="#fff"/></svg>
    Most Popular Public Projects
    <svg class="caret" width="10" height="6" viewBox="0 0 10 6"><path d="M0 0 5 6 10 0Z" fill="#fff"/></svg>
  </div>
  <div class="section-head" style="top:615px">
    <svg class="ico" width="12" height="15" viewBox="0 0 12 15"><path d="M1 1h7l3 3v10H1Z" fill="none" stroke="#fff" stroke-width="1.2"/><path d="M3 7h6M3 9h6M3 11h6" stroke="#fff"/></svg>
    All Public Projects
    <svg class="caret" width="10" height="6" viewBox="0 0 10 6"><path d="M0 0 5 6 10 0Z" fill="#fff"/></svg>
  </div>
</nav>

<main class="stage" role="img" aria-label="Blurred background photo of a hand reaching across a desk in warm and blue tones"></main>

<div class="notes-select">Notes<svg width="8" height="5" viewBox="0 0 8 5"><path d="M0 0 4 5 8 0Z" fill="#222"/></svg></div>

<article class="post">
  <div class="post-head">
    <div class="avatar" role="img" aria-label="Author avatar"></div>
    <div class="author">Dana Whitlock VM Cases</div>
    <div class="stamp">6/1/2017 &nbsp;at 6:63 am IST</div>
    <div class="post-links">View More &nbsp; | &nbsp; Close</div>
    <svg class="kebab" width="5" height="20" viewBox="0 0 5 20"><rect y="0" width="5" height="5" rx="1" fill="#999"/><rect y="7.5" width="5" height="5" rx="1" fill="#999"/><rect y="15" width="5" height="5" rx="1" fill="#999"/></svg>
  </div>
  <div class="post-body">
    <p>Welcome to the Velmora 'Startup Starter Kit' - do more better!</p>
    <p>We the team at Velmora have been used the assets and structure in this kit across several startups. Most of what you will find here are things that will help you get started in your earliest phases.</p>
    <p>We recommend you look though the structure of this project as a an organizational logic, and then dig into some of the documentation templates.</p>
    <p>Best of luck on your venture, and please let us know if we can help!</p>
    <p>TMP - General Business Scrum Template</p>
    <div class="doc-link"><svg width="9" height="11" viewBox="0 0 9 11"><path d="M0 0h6l3 3v8H0Z" fill="#2a9fd6"/><path d="M2 5h5M2 7h5M2 9h5" stroke="#fff" stroke-width=".8"/></svg>https://docs.example-suite.net/document/d/1xVXJPiTakOMzbHq380Mn1g4W7yq84n3UdiU1MJYhdwY/edit</div>
  </div>
  <div class="scrollbar"></div>
</article>

<div class="composer">Type here...
  <div class="round-btn" style="left:718px"><svg width="12" height="11" viewBox="0 0 12 11"><ellipse cx="6" cy="4.5" rx="6" ry="4.5" fill="#fff"/><path d="M2 7 1 11 5 8.5Z" fill="#fff"/></svg></div>
  <div class="round-btn" style="left:754px"><svg width="13" height="13" viewBox="0 0 13 13"><path d="M5.5 7.5a2.5 2.5 0 0 0 3.5 0l2.5-2.5a2.5 2.5 0 0 0-3.5-3.5L7 2.5M7.5 5.5a2.5 2.5 0 0 0-3.5 0L1.5 8a2.5 2.5 0 0 0 3.5 3.5L6 10.5" fill="none" stroke="#fff" stroke-width="1.5"/></svg></div>
  <div class="round-btn" style="left:790px"><svg width="13" height="11" viewBox="0 0 13 11"><path d="M0 2.5h3.5L5 0.5h3l1.5 2H13V11H0Z" fill="#fff"/><circle cx="6.5" cy="6.5" r="2.4" fill="#36434f"/></svg></div>
  <div class="round-btn" style="left:826px"><svg width="10" height="13" viewBox="0 0 10 13"><path d="M1 1h5l3 3v8H1Z" fill="none" stroke="#fff" stroke-width="1.3"/></svg></div>
</div>

<footer class="app-footer">Copyright &nbsp;© &nbsp;2017 &nbsp;Velmora. &nbsp; All rights reserved.<span class="build-tag">M2</span></footer>
</body>
</html>
```